Book cover design for the book titled "Quieter Under Lanterns."

create a book cover. The book title is, "Quieter Under Lanterns: A Ledger of Harbour Songs Across Mild Winters." The purpose of the book is to create awareness of how childhood trauma is impacting 7 out of 10 adults in the world today and that two-thirds of children will experience neglect and or abuse before their 18th birthday. One victim described that his mental and physical illness resulting from childhood trauma felt like he wa being pulled to the ground, that the force was "quieter under lanterns." The design should be clean and simple and communicate a crisis.

```html
<!DOCTYPE html>
<html lang="en">
<head>
<meta charset="utf-8">
<title>Quieter Under Lanterns — Book Cover</title>
<link rel="stylesheet" href="https://fonts.googleapis.com/css2?family=Archivo+Narrow:wght@400;500&family=Inter:wght@400&display=swap">
<style>
  :root {
    --mat-tan: #bfa17a;
    --night: #050707;
    --moon: #cfcfc9;
    --ink: #232021;
    --paper-white: #ffffff;
    --figure-shade: #6e6c69;
  }
  html, body {
    margin: 0;
    padding: 0;
    width: 927px;
    height: 1200px;
    overflow: hidden;
    background: var(--mat-tan);
  }
  .artboard {
    position: relative;
    width: 927px;
    height: 1200px;
    background: var(--mat-tan);
  }
  .cover {
    position: absolute;
    left: 147px;
    top: 191px;
    width: 613px;
    height: 792px;
    display: block;
  }
  .tagline {
    font-family: "Archivo Narrow", sans-serif;
    font-weight: 500;
    font-size: 22px;
    fill: var(--paper-white);
  }
  .title {
    font-family: "Inter", sans-serif;
    font-weight: 400;
    font-size: 80px;
    letter-spacing: -1px;
  }
  .subtitle {
    font-family: "Archivo Narrow", sans-serif;
    font-weight: 500;
    font-size: 26px;
  }
  .on-night { fill: var(--moon); }
  .on-moon { fill: var(--ink); }
</style>
</head>
<body>
<div class="artboard">
  <svg class="cover" viewBox="0 0 613 792" xmlns="http://www.w3.org/2000/svg">
    <defs>
      <clipPath id="night-side">
        <path d="M0 0 H393 C230 100 140 260 145 413 C150 570 220 690 290 792 H0 Z"/>
      </clipPath>
      <clipPath id="moon-side">
        <path d="M393 0 H613 V792 H290 C220 690 150 570 145 413 C140 260 230 100 393 0 Z"/>
      </clipPath>
    </defs>

    <rect class="moon-field" width="613" height="792" fill="var(--moon)"/>
    <path class="night-field" d="M0 0 H393 C230 100 140 260 145 413 C150 570 220 690 290 792 H0 Z" fill="var(--night)"/>

    <rect class="figures-illustration" role="img"
          aria-label="Silhouette illustration: an adult reaching toward a child who hangs from a rope, being pulled downward"
          x="145" y="0" width="433" height="570" fill="var(--figure-shade)" opacity="0.45"/>

    <text class="tagline" x="41" y="74">CREATE AWARENESS OF</text>
    <text class="tagline" x="41" y="102">HOW CHILDHOOD TRAUMA</text>

    <g class="title-block" clip-path="url(#night-side)">
      <text class="title on-night" x="34" y="464">QUIETER</text>
      <text class="title on-night" x="34" y="538">UNDER</text>
      <text class="title on-night" x="34" y="611">LANTERNS</text>
      <text class="subtitle on-night" x="36" y="682" textLength="420" lengthAdjust="spacingAndGlyphs">A LEDGER OF HARBOUR SONGS ACROSS MILD WINTERS</text>
    </g>
    <g class="title-block" clip-path="url(#moon-side)">
      <text class="title on-moon" x="34" y="464">QUIETER</text>
      <text class="title on-moon" x="34" y="538">UNDER</text>
      <text class="title on-moon" x="34" y="611">LANTERNS</text>
      <text class="subtitle on-moon" x="36" y="682" textLength="420" lengthAdjust="spacingAndGlyphs">A LEDGER OF HARBOUR SONGS ACROSS MILD WINTERS</text>
    </g>
  </svg>
</div>
</body>
</html>
```